Whistleblowing, Privacy & Police State conference banner ad

We are looking to have a banner ad designed for a conference we are holding in February called Keystone Summit. Keystone Summit is an annual conference (now in its 7th year) held in Nashua, New Hampshire which focused on various aspects of liberty and for 2014 or primary focus is whistleblowing and privacy issues particularly an examination of the recent QRB revelations.

The banner ad should be 728 X 90 (but we would like to be able to use it across different properties so an ad which is easily adapted to other dimensions would be ideal), animation is possible (gif/swf) but not essential if you can make a static banner work go for it.

All the conference information is available on http://brightgatesummit.example/ and other information about our organization which might help you is available at http://openmeadowalliance.example/.

We would like source files from the winner (PSD, AI etc) so please keep that in mind. Art assets are attached to the project for the event and organization logos.

Target Market(s)

Those who care about privacy, libertarians, politically inclined, Zentra people, those interested in technology, those interested in QRB issues etc.

Industry/Entity Type

Event

Requirements
Must have
• Event logo, any of the available designs.

Design should shout the event theme, we want it to be clear what this conference is about.
Nice to have
• If our organization logo can be included that would be ideal but not strictly necessary if it doesn't make sense with your concept, designs will not be penalized for not including this.

Any of the speaker names from http://brightgatesummit.example/ particularly those listed under "primary". Other names not currently listed that could be included are Tom Revel, Mark Delaney, Paul d'Arcenne and Tibor Markham. This is another point where inclusion is optional, if you think the design is strong enough without including any names then don't include them.

Location, Date etc. Again optional based on if it fits with the design

```html
<!DOCTYPE html>
<html lang="en">
<head>
<meta charset="utf-8">
<title>Collecting Your Data — Keystone Summit banner</title>
<link rel="stylesheet" href="https://fonts.googleapis.com/css2?family=Share+Tech+Mono&display=swap">
<style>
  :root {
    --green-deep: #0f4a0a;
    --green-mid: #2f9a1c;
    --green-bright: #5fd43a;
    --green-glow: #9dff7a;
    --ink-white: #f4fff0;
    --scan-dark: rgba(0, 30, 0, 0.35);
  }
  html, body {
    margin: 0;
    padding: 0;
    width: 1200px;
    height: 148px;
    overflow: hidden;
    background: var(--green-deep);
  }
  .banner {
    position: relative;
    width: 1200px;
    height: 148px;
    overflow: hidden;
    background: radial-gradient(ellipse 70% 90% at 45% 50%, var(--green-bright) 0%, var(--green-mid) 45%, var(--green-deep) 100%);
    font-family: "Share Tech Mono", monospace;
  }
  .banner__streaks {
    position: absolute;
    inset: 0;
    background: repeating-linear-gradient(90deg,
      rgba(180, 255, 150, 0.10) 0 3px,
      transparent 3px 9px,
      rgba(0, 40, 0, 0.12) 9px 11px,
      transparent 11px 17px);
  }
  .banner__scanlines {
    position: absolute;
    inset: 0;
    background: repeating-linear-gradient(0deg, var(--scan-dark) 0 2px, transparent 2px 5px);
    pointer-events: none;
  }
  .banner__glitch-band {
    position: absolute;
    left: 0;
    right: 0;
    height: 10px;
    background: rgba(200, 255, 180, 0.12);
  }
  .banner__glitch-band--a { top: 40px; }
  .banner__glitch-band--b { top: 96px; height: 6px; }
  .folder-icon {
    position: absolute;
    left: 66px;
    top: 25px;
    width: 115px;
    height: 66px;
    opacity: 0.55;
  }
  .cursor-icon {
    position: absolute;
    left: 198px;
    top: 49px;
    width: 57px;
    height: 91px;
  }
  .headline {
    margin: 0;
    font-weight: 400;
    color: var(--ink-white);
    text-shadow: 0 0 6px var(--green-glow), 0 0 14px rgba(157, 255, 122, 0.7), -6px 0 2px rgba(255, 255, 255, 0.25);
  }
  .headline__lead,
  .headline__rest {
    position: absolute;
    white-space: nowrap;
    line-height: 1;
  }
  .headline__lead {
    left: 255px;
    top: 30px;
    font-size: 96px;
    letter-spacing: 2px;
  }
  .headline__rest {
    left: 796px;
    top: 64px;
    font-size: 40px;
    letter-spacing: 2px;
  }
  .event-mark {
    position: absolute;
    left: 1080px;
    top: 56px;
    display: flex;
    align-items: center;
    gap: 8px;
    color: var(--ink-white);
    font-size: 15px;
    line-height: 1.15;
    letter-spacing: 1px;
    text-transform: uppercase;
  }
  .event-mark__square {
    width: 14px;
    height: 14px;
    background: var(--ink-white);
    flex: none;
  }
</style>
</head>
<body>
  <div class="banner">
    <div class="banner__streaks"></div>

    <svg class="folder-icon" viewBox="0 0 104 72" aria-hidden="true">
      <path d="M2 8 H36 L44 16 H102 V70 H2 Z" fill="#8fe06a" stroke="#c8ffb0" stroke-width="2"/>
      <path d="M2 24 H102 V70 H2 Z" fill="#6cc84a"/>
    </svg>

    <svg class="cursor-icon" viewBox="0 0 54 86" aria-hidden="true">
      <path d="M4 4 L4 66 L18 52 L30 80 L40 75 L28 48 L48 48 Z"
            fill="#ffffff" stroke="#1a3a12" stroke-width="3" stroke-linejoin="round"/>
    </svg>

    <h1 class="headline">
      <span class="headline__lead">Collecting</span>
      <span class="headline__rest">Your Data...</span>
    </h1>

    <div class="event-mark">
      <span class="event-mark__square"></span>
      <span class="event-mark__name">Keystone<br>Summit</span>
    </div>

    <div class="banner__glitch-band banner__glitch-band--a"></div>
    <div class="banner__glitch-band banner__glitch-band--b"></div>
    <div class="banner__scanlines"></div>
  </div>
</body>
</html>
```